Jewelry Shop Needs a Business Card Design

***We want a very sharp and unforgettable pantone for the Business Card. ***
***We do not want the business card or logo only in black, white and grey color!!!Please provide us a main color as our brand topic! Thanks!! ***

Mabel’s Nook is a Hong Kong based fine jewelry brand.

We want a very nice, simple and elegant business card design for Mabel's Nook Brand. The company's logo has been uploaded already.

You can design with below info:

Dorian Fung
Director
M: +852 94273658
T: +852 35820417
F: +852 35820419
E: dorian.fung@mabelsnook.example
5/F , Harbourlight Tower, 12-18 Orchid Lane, Wan Tung Kok, Kowloon, Hong Kong

Target Market(s)

Mabel’s Nook philosophy is a jewelry icon of young, creative, trendy, fashionable, stylish, energetic, and elegant. For Mabel’s Nook, jewelry is one collection of artworks, the most important items in personal life.

Industry/Entity Type

Jewelry

Requirements
Must have
• We want a very sharp and unforgettable pantone for the Business Card.

```html
<!DOCTYPE html>
<html lang="en">
<head>
<meta charset="utf-8">
<title>Mabel’s Nook — Business Card</title>
<link rel="stylesheet" href="https://fonts.googleapis.com/css2?family=Cinzel:wght@400;500&display=swap">
<style>
  :root {
    --backdrop: #e9e6e1;
    --brand-light: #2a9aa3;
    --brand-mid: #137080;
    --brand-deep: #073843;
    --edge-1: #0a4a57;
    --edge-2: #063440;
    --ink-light: #f5f3ee;
    --ink-soft: #d7ecec;
    --accent: #e2c98f;
    --mark-light: #ffffff;
    --mark-dark: #04242c;
  }
  html, body {
    margin: 0;
    width: 1200px;
    height: 913px;
    overflow: hidden;
    background: var(--backdrop);
    font-family: "Cinzel", "Times New Roman", serif;
  }
  .canvas {
    position: relative;
    width: 1200px;
    height: 913px;
  }
  .card {
    position: absolute;
    width: 560px;
    height: 320px;
    border-radius: 3px;
    background: linear-gradient(200deg, var(--brand-light) 0%, var(--brand-mid) 50%, var(--brand-deep) 100%);
    box-shadow: 0 3px 0 var(--edge-1), 0 6px 0 var(--edge-2), 0 10px 24px rgba(0,0,0,.25);
    overflow: hidden;
  }
  .card--front { left: 60px; top: 90px; }
  .card--back { left: 580px; top: 500px; }

  .brand {
    position: absolute;
    display: flex;
    flex-direction: column;
    align-items: center;
  }
  .brand__disc {
    border-radius: 50%;
  }
  .brand__name {
    letter-spacing: 0.06em;
    white-space: nowrap;
  }
  .card--front .brand {
    left: 0; right: 0; top: 62px;
  }
  .card--front .brand__disc {
    width: 128px; height: 128px;
    background: var(--mark-light);
  }
  .card--front .brand__name {
    margin-top: 34px;
    font-size: 26px;
    color: var(--ink-light);
  }

  .card--back .brand {
    left: 56px; top: 104px;
  }
  .card--back .brand__disc {
    width: 96px; height: 96px;
    background: var(--mark-dark);
  }
  .card--back .brand__name {
    margin-top: 18px;
    font-size: 17px;
    color: var(--accent);
  }

  .contact {
    position: absolute;
    left: 292px; top: 44px;
    color: var(--ink-soft);
    font-size: 12px;
    line-height: 1.45;
  }
  .contact__name {
    font-size: 17px;
    color: var(--ink-light);
    margin: 0;
  }
  .contact__role {
    font-size: 10px;
    color: var(--accent);
    margin: 0 0 16px;
  }
  .contact__lines, .contact__address {
    margin: 0 0 16px;
    font-style: normal;
  }
</style>
</head>
<body>
<main class="canvas">
  <section class="card card--front" aria-label="Card front">
    <div class="brand">
      <div class="brand__disc"></div>
      <div class="brand__name">Mabel’s Nook</div>
    </div>
  </section>

  <section class="card card--back" aria-label="Card back">
    <div class="brand">
      <div class="brand__disc"></div>
      <div class="brand__name">Mabel’s Nook</div>
    </div>
    <div class="contact">
      <p class="contact__name">Dorian Fung</p>
      <p class="contact__role">Director</p>
      <p class="contact__lines">
        M: +852 94273658<br>
        T: +852 35820417<br>
        F: +852 35820419<br>
        E: dorian.fung@mabelsnook.example
      </p>
      <address class="contact__address">
        5/F , Harbourlight Tower,<br>
        12-18 Orchid Lane, Wan Tung Kok,<br>
        Kowloon, Hong Kong
      </address>
    </div>
  </section>
</main>
</body>
</html>
```